Vosh CBD Pod package and logo design.

Vosh is the brand name for our line of CBD Plim style pods. I would like the logo to be designed as well as the packaging. The packaging will be the same size as the Plim pod packaging. I would also like the box to be white and have a similar clean look just as Plim does. My vision for the brand is very simple with black letters in a font similar to the picture attached. I would also like an animated marijuana flower that is extremely simple and also very similar to the picture attached below. Please note that I do not want the logo to be an exact copy of the example attached. I have also attached a picture of the Plim packaging.

Although I do like my idea of the logo I am very much open to your creative ideas and will absolutely consider any other logo designs outside of my description. One final note, outside of the simple marijuana flower above the "i", I do not want the logo to scream "Marijuana" as it is a CBD product and the overt marijuana referenced brands dont fair to well to the non-marijuana user. If you have any questions, please do not hesitate to ask.

```html
<!DOCTYPE html>
<html lang="en">
<head>
<meta charset="utf-8">
<title>Vosh Pod Packaging</title>
<link href="https://fonts.googleapis.com/css2?family=Open+Sans:wght@300;400;600;700;800&family=Tenor+Sans&display=swap" rel="stylesheet">
<style>
  :root {
    --backdrop: #a7a9ac;
    --box: #fbfbfb;
    --ink: #3d3d3f;
    --slate: #5a5c78;
    --teal: #2fb5b0;
    --pod-green: #66bd80;
    --pod-dark: #4b4e4a;
    --white: #ffffff;
  }
  * { margin: 0; padding: 0; box-sizing: border-box; }
  html, body { width: 1200px; height: 704px; overflow: hidden; }
  body {
    background: var(--backdrop);
    position: relative;
    font-family: "Open Sans", sans-serif;
    color: var(--ink);
  }
  .package {
    position: absolute;
    top: 58px;
    width: 339px;
    height: 587px;
    background: var(--box);
  }
  .package--bold { left: 62px; }
  .package--light { left: 429px; }
  .package--classic { left: 801px; }

  .brand {
    position: absolute;
    color: var(--ink);
    font-family: "Open Sans", sans-serif;
    line-height: 1;
    white-space: nowrap;
  }
  .package--bold .brand { left: 24px; top: 36px; font-size: 78px; font-weight: 800; letter-spacing: 0; }
  .package--light .brand { left: 34px; top: 24px; font-size: 96px; font-weight: 300; }
  .package--classic .brand { left: 0; width: 100%; text-align: center; top: 34px; font-size: 112px; font-weight: 400; }

  .brand-dot {
    position: absolute;
    left: 256px;
    top: 32px;
    width: 58px;
    height: 58px;
    border-radius: 50%;
    background: var(--teal);
  }

  .spec {
    position: absolute;
    left: 0;
    color: var(--white);
    font-size: 19px;
    line-height: 1;
    display: flex;
    align-items: center;
    padding-left: 14px;
    white-space: nowrap;
  }
  .spec--count { background: var(--slate); font-weight: 600; }
  .spec--strength { background: var(--teal); font-weight: 400; }

  .package--bold .spec--count { top: 182px; width: 116px; height: 27px; font-size: 20px; }
  .package--bold .spec--strength { top: 216px; width: 191px; height: 29px; font-size: 20px; }
  .package--light .spec--count,
  .package--classic .spec--count { top: 174px; width: 103px; height: 26px; }
  .package--light .spec--strength,
  .package--classic .spec--strength { top: 200px; width: 166px; height: 26px; font-size: 18px; }
  .package--classic .spec { left: 12px; }

  .pods-placeholder {
    position: absolute;
    left: 28px;
    width: 282px;
    height: 125px;
    border-radius: 3px;
    background: linear-gradient(to bottom, var(--pod-green) 0%, var(--pod-green) 48%, var(--pod-dark) 52%, var(--pod-dark) 100%);
  }
  .package--bold .pods-placeholder { top: 277px; }
  .package--light .pods-placeholder,
  .package--classic .pods-placeholder { top: 266px; }

  .tagline {
    position: absolute;
    top: 432px;
    left: 0;
    width: 100%;
    text-align: center;
    font-size: 12px;
  }
  .warning {
    position: absolute;
    top: 449px;
    left: 25px;
    width: 289px;
    height: 113px;
    border: 1px solid var(--ink);
    font-family: "Tenor Sans", sans-serif;
    font-size: 16px;
    line-height: 23px;
    text-align: center;
    letter-spacing: 1px;
    text-transform: uppercase;
    padding-top: 9px;
  }
  .warning__title { display: block; text-transform: none; letter-spacing: 0.5px; }
</style>
</head>
<body>

<section class="package package--bold">
  <div class="brand">VOSH</div>
  <span class="brand-dot"></span>
  <div class="spec spec--count">4 Pods</div>
  <div class="spec spec--strength">5.0% Strength</div>
  <div class="pods-placeholder" role="img" aria-label="Illustration of four vape pods with green tops and dark bases"></div>
  <p class="tagline">The Alternative For Adults Smokers</p>
  <p class="warning"><span class="warning__title">WARNING!</span>This product contains nicotine. Nicotine is an addictive chemical</p>
</section>

<section class="package package--light">
  <div class="brand">vosh</div>
  <span class="brand-dot"></span>
  <div class="spec spec--count">4 Pods</div>
  <div class="spec spec--strength">5.0% Strength</div>
  <div class="pods-placeholder" role="img" aria-label="Illustration of four vape pods with green tops and dark bases"></div>
  <p class="tagline">The Alternative For Adults Smokers</p>
  <p class="warning"><span class="warning__title">WARNING!</span>This product contains nicotine. Nicotine is an addictive chemical</p>
</section>

<section class="package package--classic">
  <div class="brand">vosh</div>
  <div class="spec spec--count">4 Pods</div>
  <div class="spec spec--strength">5.0% Strength</div>
  <div class="pods-placeholder" role="img" aria-label="Illustration of four vape pods with green tops and dark bases"></div>
  <p class="tagline">The Alternative For Adults Smokers</p>
  <p class="warning"><span class="warning__title">WARNING!</span>This product contains nicotine. Nicotine is an addictive chemical</p>
</section>

</body>
</html>
```